Corporate Brightfen business cards to be handed to investor, bankers etc. Needs to have a young feel

I need business cards designed for a technology company that provides uber-like rapid response on the security industry. I would like it simple but very cool and tasteful. See attached documents for artwork and colours to be used. Cut sheet describes business model. Card stock should be thicker than normal. I would like the one side to be just the art and the other to have the contact info with maybe the pin somewhere.

Target Market(s)

Investors

Industry/Entity Type

Business

Contact Information for Business Card

Would like the logo attached on one side with name address and other info on the other side.

Font styles to use
Other font styles liked:
• See existing logo

Colors
6b449b
886aae
e4daeb
ffffff

Requirements
Must have
• Name: Dorian Felkatsis
• Address: 47 Larkfield Avenue, Toronto, On, M6K2B7
• Tel: 416-7291846
• Email: rolo@brightfen.io
Nice to have
• See logo colours

```html
<!DOCTYPE html>
<html lang="en">
<head>
<meta charset="utf-8">
<title>Brightfen Business Cards</title>
<link href="https://fonts.googleapis.com/css2?family=Montserrat:wght@500;600&display=swap" rel="stylesheet">
<style>
  :root {
    --purple: #886aae;
    --purple-deep: #6b449b;
    --ink: #1d1b1c;
    --text-grey: #555458;
    --paper: #ffffff;
    --backdrop: #d9d9db;
  }
  * { margin: 0; padding: 0; box-sizing: border-box; }
  html, body { width: 1200px; height: 900px; overflow: hidden; }
  body { background: var(--backdrop); position: relative; }

  .card {
    position: absolute;
    width: 597px;
    height: 340px;
    background: var(--paper);
    border-radius: 18px;
    overflow: hidden;
  }
  .card-front { left: 293px; top: 88px; }
  .card-back { left: 283px; top: 462px; }

  .card-art { position: absolute; inset: 0; }

  .company-name {
    position: absolute;
    font-family: "Montserrat", sans-serif;
    font-weight: 500;
    color: var(--ink);
    white-space: nowrap;
  }
  .company-name-front {
    left: 0; right: 0; top: 128px;
    text-align: center;
    font-size: 56px;
    line-height: 84px;
  }
  .company-name-back {
    right: 47px; top: 32px;
    font-size: 32px;
    line-height: 46px;
  }

  .person-name {
    position: absolute;
    left: 44px; top: 124px;
    font-family: "Montserrat", sans-serif;
    font-weight: 600;
    font-size: 25px;
    color: var(--purple);
  }
  .contact-list {
    position: absolute;
    left: 43px; top: 168px;
    list-style: none;
  }
  .contact-item {
    display: flex;
    align-items: center;
    gap: 8px;
    height: 28px;
    font-family: "Montserrat", sans-serif;
    font-weight: 600;
    font-size: 17px;
    color: var(--text-grey);
  }
  .contact-icon { width: 26px; height: 26px; flex: none; }

  .address-band {
    position: absolute;
    left: 0; bottom: 0;
    width: 597px; height: 56px;
  }
  .address {
    position: absolute;
    left: 170px; bottom: 14px;
    font-family: "Montserrat", sans-serif;
    font-weight: 500;
    font-size: 18px;
    color: var(--paper);
    white-space: nowrap;
  }
</style>
</head>
<body>

<section class="card card-front" aria-label="Business card front">
  <svg class="card-art" width="597" height="340" viewBox="0 0 597 340" aria-hidden="true">
    <polygon points="0,147 111,147 102,180 0,180" fill="var(--purple)"/>
    <polygon points="0,184 100,184 96,194 0,194" fill="var(--purple)"/>
    <polygon points="500,147 597,147 597,180 491,180" fill="var(--purple)"/>
    <polygon points="490,184 597,184 597,194 487,194" fill="var(--purple)"/>
  </svg>
  <p class="company-name company-name-front">Brightfen</p>
</section>

<section class="card card-back" aria-label="Business card back">
  <p class="company-name company-name-back">Brightfen</p>

  <h1 class="person-name">Dorian Felkatsis</h1>

  <ul class="contact-list">
    <li class="contact-item">
      <svg class="contact-icon" viewBox="0 0 26 26" aria-hidden="true">
        <circle cx="13" cy="13" r="12" fill="none" stroke="var(--purple)" stroke-width="1.5"/>
        <path d="M10 7.5c-1.5 1-1.8 3-1 5.5s2.5 4.5 4.3 5.5c1.3.7 2.6.3 3.3-.6l-1.7-2.2c-.5.3-1 .4-1.5 0-.9-.8-1.8-2.5-2-3.6-.1-.5.2-.9.7-1.1l-.5-2.8z" fill="var(--purple)"/>
      </svg>
      416-7291846
    </li>
    <li class="contact-item">
      <svg class="contact-icon" viewBox="0 0 26 26" aria-hidden="true">
        <circle cx="13" cy="13" r="12" fill="none" stroke="var(--purple)" stroke-width="1.5"/>
        <rect x="7" y="9" width="12" height="8.5" fill="none" stroke="var(--purple)" stroke-width="1.4"/>
        <path d="M7 9l6 5 6-5" fill="none" stroke="var(--purple)" stroke-width="1.4"/>
      </svg>
      rolo@brightfen.io
    </li>
    <li class="contact-item">
      <svg class="contact-icon" viewBox="0 0 26 26" aria-hidden="true">
        <circle cx="13" cy="13" r="12" fill="none" stroke="var(--purple)" stroke-width="1.5"/>
        <circle cx="13" cy="13" r="7" fill="none" stroke="var(--purple)" stroke-width="1.2"/>
        <ellipse cx="13" cy="13" rx="3" ry="7" fill="none" stroke="var(--purple)" stroke-width="1.2"/>
        <path d="M6 13h14M7 9.5h12M7 16.5h12" stroke="var(--purple)" stroke-width="1.1"/>
      </svg>
      www.brightfen.io
    </li>
  </ul>

  <svg class="address-band" viewBox="0 0 597 56" aria-hidden="true">
    <polygon points="0,0 138,0 118,56 0,56" fill="var(--ink)"/>
    <polygon points="146,0 597,0 597,56 126,56" fill="var(--purple)"/>
  </svg>
  <p class="address">47 Larkfield Avenue, Toronto, On, M6K2B7</p>
</section>

</body>
</html>
```